DOUBLE SIDED BROCHURE NEEDED TO PROMOTE DOCTOR

I need a double sided DL size (99mm x 210mm) brochure, promoting a doctor seeing patients in a new area.

I want something professional. I have included the relevant information. I would also like the Dr's picture somwhere in the brochure, with a professional background. I wish to print these tomorrow, so i will pick a winner within 14 hours of posting this ad.

I have included an example of a brochures design that I recently saw, and its definietly a good starting point.

Medical

```html
<!DOCTYPE html>
<html lang="en">
<head>
<meta charset="utf-8">
<title>Dr. Samir Nadeem – DL Brochure</title>
<link href="https://fonts.googleapis.com/css2?family=Bebas+Neue&family=Arimo:wght@400;700&family=Open+Sans:wght@300;400;700&display=swap" rel="stylesheet">
<style>
  :root{
    --bg:#d3dad6;
    --navy:#22304a;
    --charcoal:#383b42;
    --teal:#7dbac6;
    --teal-text:#4f95a3;
    --lime:#c5da2c;
    --ice:#dff3f6;
    --paper:#f4f5f5;
    --ink:#2c2c2c;
    --white:#ffffff;
  }
  *{margin:0;padding:0;box-sizing:border-box}
  html,body{width:1200px;height:887px;overflow:hidden;background:var(--bg)}
  .canvas{position:relative;width:1200px;height:887px}
  .panel{position:absolute;top:22px;width:395px;height:839px;overflow:hidden;box-shadow:0 2px 8px rgba(0,0,0,.18)}
  .panel--front{left:157px;background:var(--ice)}
  .panel--back{left:636px;background:var(--paper)}
  .panel-shapes{position:absolute;inset:0;width:395px;height:839px}
  .doctor-name{position:absolute;left:11px;top:34px;font-family:'Bebas Neue',sans-serif;font-size:33px;letter-spacing:.5px;color:var(--white)}
  .clinic-address{position:absolute;font-family:'Open Sans',sans-serif;font-weight:400;font-size:13.5px;line-height:17px;color:var(--white)}
  .clinic-address svg{position:absolute;left:-30px;top:12px}
  .front-address{left:250px;top:392px}
  .back-address{left:234px;top:724px}
  .letter{position:absolute;left:52px;top:555px;width:318px;font-family:'Arimo',sans-serif;color:var(--white)}
  .letter-greeting{font-size:23px;font-weight:400;margin-bottom:6px}
  .letter-greeting strong{font-weight:700}
  .letter p{font-size:14.2px;line-height:18.5px;text-align:justify;margin-bottom:18px}
  .phone{position:absolute;font-family:'Open Sans',sans-serif;font-size:20px;color:var(--white);display:flex;align-items:center;gap:10px}
  .front-phone{left:92px;top:745px}
  .back-phone{left:154px;top:808px}
  .referral-note{position:absolute;left:20px;top:806px;font-family:'Open Sans',sans-serif;font-weight:700;font-size:12.5px;color:var(--teal)}
  .intro{position:absolute;left:25px;top:310px;width:345px;font-family:'Arimo',sans-serif;font-size:19px;line-height:23.5px;color:var(--teal-text)}
  .services{position:absolute;left:55px;list-style:none;font-family:'Arimo',sans-serif;font-size:15px;line-height:22.8px;color:var(--ink)}
  .services li{position:relative;padding-left:20px}
  .services li::before{content:"";position:absolute;left:0;top:9px;width:5px;height:5px;border-radius:50%;background:var(--ink)}
  .services--specialist{top:400px;width:300px}
  .services--general{top:568px}
  .subheading{position:absolute;left:28px;top:534px;font-family:'Arimo',sans-serif;font-size:19px;color:var(--teal-text)}
</style>
</head>
<body>
<main class="canvas">

  <!-- Front side -->
  <section class="panel panel--front">
    <svg class="panel-shapes" viewBox="0 0 395 839">
      <defs>
        <linearGradient id="portraitTone" x1="0" y1="0" x2="0" y2="1">
          <stop offset="0" stop-color="#b7b2ab"/>
          <stop offset=".55" stop-color="#8c7a6d"/>
          <stop offset="1" stop-color="#2a2f44"/>
        </linearGradient>
      </defs>
      <rect class="portrait" x="100" y="30" width="295" height="390" fill="url(#portraitTone)" role="img" aria-label="Portrait photograph of the doctor in a dark jacket"/>
      <polygon points="0,118 190,70 230,70 0,150" fill="#a9d6df"/>
      <polygon points="0,0 330,0 150,96 0,96" fill="var(--navy)"/>
      <polygon points="300,0 330,0 290,20 270,20" fill="var(--teal)"/>
      <polygon points="100,380 395,315 395,545 190,420" fill="var(--navy)"/>
      <polygon points="0,307 0,536 190,418" fill="var(--teal)"/>
      <rect x="25" y="345" width="35" height="150" rx="6" fill="#a7d4de" role="img" aria-label="Medical staff emblem"/>
      <polygon points="0,536 190,418 395,540 395,839 0,839" fill="var(--charcoal)"/>
      <line x1="0" y1="307" x2="395" y2="538" stroke="var(--lime)" stroke-width="3"/>
      <polygon points="28,590 42,582 42,598" fill="var(--teal)"/>
      <polygon points="0,790 305,790 340,839 0,839" fill="var(--navy)"/>
      <polygon points="305,790 395,790 395,839 340,839" fill="var(--teal)"/>
    </svg>
    <h1 class="doctor-name">Dr. Samir Nadeem</h1>
    <address class="clinic-address front-address">
      <svg width="14" height="18" viewBox="0 0 14 18"><path d="M7 1a6 6 0 0 0-6 6c0 4.5 6 10 6 10s6-5.5 6-10a6 6 0 0 0-6-6z" fill="none" stroke="var(--lime)" stroke-width="2"/><circle cx="7" cy="7" r="2" fill="var(--lime)"/></svg>
      Coralbay Clinic:<br>42 Harbourview Road<br>Coralbay WA 6999.
    </address>
    <div class="letter">
      <h2 class="letter-greeting"><strong>Dear</strong> Doctors,</h2>
      <p>We are pleased to announce that Dr. Samir Nadeem is now consulting in Coralbay, seeing public and private patients.</p>
      <p>Guaranteed appointment within two weeks, with patients having the option of surgery at Westbay Health Campus, Harbour Ridge Hospital or St. Clement Southvale.</p>
    </div>
    <div class="phone front-phone">
      <svg width="18" height="18" viewBox="0 0 24 24"><path d="M6.6 10.8a15 15 0 0 0 6.6 6.6l2.2-2.2c.3-.3.7-.4 1-.2 1.1.4 2.3.6 3.6.6.6 0 1 .4 1 1V20c0 .6-.4 1-1 1A17 17 0 0 1 3 4c0-.6.4-1 1-1h3.5c.6 0 1 .4 1 1 0 1.3.2 2.5.6 3.6.1.3 0 .7-.2 1z" fill="var(--lime)"/></svg>
      Phone: 1300 482 316
    </div>
    <p class="referral-note">Please send all referrals by fax to (08) 6000 4821.</p>
  </section>

  <!-- Back side -->
  <section class="panel panel--back">
    <svg class="panel-shapes" viewBox="0 0 395 839">
      <defs>
        <linearGradient id="emblemTone" x1="0" y1="0" x2="1" y2="1">
          <stop offset="0" stop-color="#3f5d94"/>
          <stop offset="1" stop-color="#c5da2c"/>
        </linearGradient>
        <linearGradient id="footerTone" x1="0" y1="0" x2="1" y2="1">
          <stop offset="0" stop-color="#1e2432"/>
          <stop offset="1" stop-color="#263a55"/>
        </linearGradient>
      </defs>
      <rect x="160" y="40" width="235" height="270" rx="20" fill="url(#emblemTone)" opacity=".35" role="img" aria-label="Hexagon network graphic with a medical cross and heartbeat"/>
      <polygon points="0,118 190,70 230,70 0,160" fill="#a9d6df"/>
      <polygon points="0,0 330,0 150,96 0,96" fill="var(--navy)"/>
      <polygon points="300,0 330,0 290,20 270,20" fill="var(--teal)"/>
      <polygon points="0,777 395,614 395,839 0,839" fill="url(#footerTone)"/>
      <line x1="0" y1="777" x2="395" y2="614" stroke="var(--lime)" stroke-width="4"/>
    </svg>
    <h1 class="doctor-name">Dr. Samir Nadeem</h1>
    <p class="intro">Dr. Nadeem is a highly trained specialised surgeon, in all areas of Endocrine, Breast and General Surgery. Including;</p>
    <ul class="services services--specialist">
      <li>Thyroid Surgery</li>
      <li>Parathyroid surgery (including minimally invasive parathyroidectomy)</li>
      <li>Breast Cancer</li>
      <li>Benign breast lesions</li>
    </ul>
    <h2 class="subheading">All areas of general surgery, such as;</h2>
    <ul class="services services--general">
      <li>Gallbladder surgery</li>
      <li>Hernia surgery</li>
      <li>Haemorrhoids</li>
      <li>Carpal Tunnel</li>
      <li>Vasectomy etc etc…</li>
    </ul>
    <address class="clinic-address back-address">
      <svg width="14" height="18" viewBox="0 0 14 18"><path d="M7 1a6 6 0 0 0-6 6c0 4.5 6 10 6 10s6-5.5 6-10a6 6 0 0 0-6-6z" fill="none" stroke="var(--lime)" stroke-width="2"/><circle cx="7" cy="7" r="2" fill="var(--lime)"/></svg>
      Coralbay Clinic:<br>42 Harbourview Road<br>Coralbay WA 6999.
    </address>
    <div class="phone back-phone">
      <svg width="18" height="18" viewBox="0 0 24 24"><path d="M6.6 10.8a15 15 0 0 0 6.6 6.6l2.2-2.2c.3-.3.7-.4 1-.2 1.1.4 2.3.6 3.6.6.6 0 1 .4 1 1V20c0 .6-.4 1-1 1A17 17 0 0 1 3 4c0-.6.4-1 1-1h3.5c.6 0 1 .4 1 1 0 1.3.2 2.5.6 3.6.1.3 0 .7-.2 1z" fill="var(--lime)"/></svg>
      Phone: 1300 482 316
    </div>
  </section>

</main>
</body>
</html>
```